Website design for dressage horse training business

Looking to develop a new website design for a dressage horse training website. We want to change from a single landing page to one with multiple pages.
You are free to use your creativity to design the main landing page. This is the only page you need to design at this point. I would encourage looking at other Dressage Training websites to get a feel for what is typically on them. A few websites are listed below although I think the design of them could be better.
Notes:
- Menu to include: Home, Services, News Room, Blog, About Us, Contact,
- FAQ section on main page
- Logo to remain the same - the logo attached is not the correct color so change to match existing color.
- Change 'Sponsors' to 'Partnerships' on main page
Here is the link to the current site:
https://lindenridgestables.com/
Example sites
https://www.crestwoodsporthorsesco.com/
https://corinnalavelledressage.com/
Target Market(s)
Older women with disposable income
Number of Pages Required
1 page
Look and feel
Each slider illustrates characteristics of the customer's brand and the style your logo design should communicate.

```html
<!DOCTYPE html>
<html lang="en">
<head>
<meta charset="utf-8">
<title>Linden Ridge Stables — Dressage &amp; Sport Horse Training</title>
<link href="https://fonts.googleapis.com/css2?family=Libre+Baskerville:wght@400;700&family=Open+Sans:wght@400;600&display=swap" rel="stylesheet">
<style>
:root{
  --dark:#464646;
  --panel:#5a5a5a;
  --faq:#5c5c5c;
  --gold:#b59a7c;
  --white:#ffffff;
  --ink:#3a3a3a;
  --muted:#9a9a9a;
  --badge:#e8e4de;
}
*{margin:0;padding:0;box-sizing:border-box}
html,body{width:1200px;height:4675px;overflow:hidden}
body{font-family:"Open Sans",sans-serif;color:var(--white);background:var(--dark);position:relative}
section,header,footer{position:absolute;left:0;width:1200px}
.abs{position:absolute}

/* nav */
.site-nav{top:0;height:100px;background:var(--dark)}
.site-nav a{position:absolute;top:42px;color:var(--white);font-size:14px;font-weight:600;text-decoration:none}
.site-nav a.active::after{content:"";position:absolute;left:0;right:0;top:26px;height:2px;background:var(--gold)}
.brand{position:absolute;left:0;width:1200px;top:22px;text-align:center;font-family:"Libre Baskerville",serif;color:var(--gold);font-size:26px;letter-spacing:2px;pointer-events:none}

/* hero */
.hero{top:100px;height:440px;background:linear-gradient(100deg,#cdbda6 0%,#bfae95 55%,#a88b6c 100%);border-bottom:4px solid var(--gold)}
.hero h1{position:absolute;left:120px;top:112px;font-size:35px;line-height:47px;font-weight:700;color:var(--white);font-family:"Libre Baskerville",serif}
.hero .place{position:absolute;left:128px;top:228px;font-size:21px;color:var(--white);display:flex;align-items:center;gap:14px}
.pill{position:absolute;height:44px;border-radius:22px;font-size:13px;font-weight:600;display:flex;align-items:center;justify-content:center}
.pill.light{left:128px;top:288px;width:136px;background:var(--white);color:var(--ink)}
.pill.gold{left:296px;top:288px;width:136px;background:var(--gold);color:var(--white)}
.emblem{left:525px;top:475px;width:150px;height:150px;border-radius:50%;background:var(--dark);border:3px solid var(--gold);z-index:3}

/* training */
.training{top:540px;height:645px;background:var(--dark)}
.section-title{position:absolute;left:0;width:1200px;text-align:center;font-family:"Libre Baskerville",serif;font-weight:700}
.training .section-title{top:95px;font-size:36px}
.training .section-title span{color:var(--gold)}
.lead{position:absolute;left:0;width:1200px;text-align:center;font-size:13px;line-height:22px;color:var(--muted)}
.training .lead{top:146px}
.offer{position:absolute;top:220px;width:405px;height:350px;background:var(--panel);border:2px solid #6d6d6d;box-shadow:0 2px 6px rgba(0,0,0,.25)}
.offer h3{position:absolute;top:50px;width:100%;text-align:center;font-size:21px;font-weight:600}
.offer p{position:absolute;left:46px;top:116px;width:310px;font-size:15px;line-height:20px}
.offer .btn{position:absolute;left:122px;top:262px;width:160px;height:42px;background:var(--gold);color:var(--white);font-size:14px;font-weight:600;display:flex;align-items:center;justify-content:center;box-shadow:0 2px 4px rgba(0,0,0,.3)}
.divider-v{left:598px;top:265px;width:3px;height:260px;background:var(--gold)}

/* about */
.about{top:1185px;height:777px;background:var(--dark)}
.about .photo{left:0;top:0;width:600px;height:777px;background:linear-gradient(160deg,#6e7a52 0%,#8d8f6a 40%,#a98a6a 70%,#d6d2c8 100%)}
.about h2{left:700px;top:70px;font-size:35px;font-weight:400;font-family:"Libre Baskerville",serif}
.about .rule{left:700px;top:118px;width:163px;height:2px;background:var(--gold)}
.social{display:flex;gap:12px}
.social i{display:block;width:22px;height:22px;border:2px solid var(--gold);border-radius:4px}
.about .social{left:980px;top:80px}
.about .copy{left:693px;top:153px;width:410px;font-size:15px;line-height:22.3px}
.about .copy p{margin-bottom:13px}

/* partnerships */
.partners{top:1962px;height:543px;background:var(--white);color:var(--ink)}
.partners .section-title{top:64px;font-size:36px;font-weight:400}
.partner{position:absolute;top:152px;width:400px}
.partner h3{font-family:"Libre Baskerville",serif;font-size:21px;font-weight:400;color:var(--gold)}
.partner p{margin-top:24px;font-size:13.5px;line-height:22px;color:#555}
.readmore{position:absolute;top:420px;font-size:13.5px;color:var(--gold);border-bottom:1px solid var(--gold);padding-bottom:3px}
.partner-badge{width:120px;height:48px;background:var(--badge);border-radius:4px}

/* for sale */
.sale{top:2505px;height:541px;background:var(--dark);border-top:4px solid var(--gold)}
.sale .section-title{top:64px;font-size:38px;color:var(--gold);font-weight:700}
.sale .sub{position:absolute;left:0;width:1200px;top:130px;display:flex;justify-content:center;align-items:center;gap:22px;color:var(--gold);font-size:15px;font-weight:600}
.sale .sub::before,.sale .sub::after{content:"";width:64px;height:2px;background:var(--gold)}
.sale .copy{left:120px;top:200px;width:580px;font-size:15px;line-height:22.5px}
.sale .copy p{margin-bottom:24px}
.sale .photo{left:800px;top:200px;width:280px;height:367px;background:linear-gradient(180deg,#d8dcd2 0%,#8a8a7a 35%,#3b2a20 70%,#2a1f18 100%);border:3px solid var(--gold);z-index:3;box-shadow:0 3px 8px rgba(0,0,0,.35)}

/* faq */
.faq{top:3046px;height:448px;background:var(--faq)}
.faq .section-title{top:72px;font-size:38px;color:#8f7a64;font-weight:700}
.bracket{left:370px;top:117px;width:460px;height:38px;border:2px solid #8f7a64;border-bottom:none}
.q{position:absolute;left:215px;width:322px;height:62px;background:var(--dark);border:2px solid #6d6d6d;font-size:14px;display:flex;align-items:center;padding-left:36px}
.answer{left:542px;top:155px;width:440px;height:202px;border:2px solid var(--gold);background:var(--dark);padding:26px 42px;font-size:12.6px;line-height:19px;color:#e4e4e4}
.arrow-dot{left:523px;top:176px;width:28px;height:28px;border-radius:50%;background:#666;border:1px solid #999;z-index:2}

/* news */
.news{top:3494px;height:706px;background:var(--white);color:var(--ink)}
.news .section-title{top:64px;font-size:36px;font-weight:400}
.news .lead{top:142px;color:#666}
.card{position:absolute;top:240px;width:285px;height:296px;background:var(--white);border:2px solid #e3c9b4;box-shadow:0 2px 6px rgba(0,0,0,.12)}
.card p{position:absolute;left:30px;top:30px;width:230px;font-size:13.5px;line-height:19px;color:#444}
.card hr{position:absolute;left:14px;top:228px;width:255px;border:none;border-top:1px solid #bbb}
.card .day{position:absolute;left:38px;top:250px;color:var(--gold);font-weight:600;font-size:15px}
.card .date{position:absolute;right:36px;top:250px;font-weight:600;font-size:16px;color:#333}
.see-more{left:525px;top:590px;width:150px;height:42px;background:var(--gold);color:var(--white);font-size:13px;font-weight:600;display:flex;align-items:center;justify-content:center;box-shadow:0 2px 4px rgba(0,0,0,.3)}

/* footer */
.footer{top:4200px;height:475px;background:var(--dark)}
.footer h2{left:122px;top:100px;font-size:25px;font-family:"Libre Baskerville",serif;font-weight:700}
.footer .rule{left:122px;top:139px;width:146px;height:2px;background:var(--gold)}
.footer .note{left:122px;top:168px;width:300px;font-size:13px;line-height:22px}
.footer .social{left:122px;top:292px}
.footer .phone{left:258px;top:293px;font-size:15px;font-weight:600}
.footer-links{left:523px;top:88px;font-size:15px;line-height:41.5px}
.map{left:716px;top:0;width:484px;height:407px;background:linear-gradient(135deg,#eae6df 0%,#e3e1d8 60%,#c7d9e3 100%)}
.zoom{left:1146px;top:310px;width:38px;height:80px;background:var(--white);box-shadow:0 1px 4px rgba(0,0,0,.3);display:flex;flex-direction:column;align-items:center;justify-content:space-around;font-size:26px;color:#555}
.legal{left:0;top:407px;width:1200px;height:68px;background:#3e3e3e;text-align:center;font-size:11px;color:#8a8a8a;line-height:68px}
</style>
</head>
<body>

<header class="site-nav">
  <a href="#" class="active" style="left:120px">Home</a>
  <a href="#" style="left:208px">Services</a>
  <a href="#" style="left:309px">About Us</a>
  <div class="brand">LINDEN RIDGE</div>
  <a href="#" style="left:824px">News Room</a>
  <a href="#" style="left:951px">Blog</a>
  <a href="#" style="left:1028px">Contact</a>
</header>

<section class="hero" role="img" aria-label="Photo of a dressage horse's legs trotting across a sand arena">
  <h1>Central Iowa's Premier Dressage<br>&amp; Sport Horse Training</h1>
  <div class="place">Located outside Maplecrest, Iowa
    <svg width="22" height="26" viewBox="0 0 22 26" fill="none" stroke="#b59a7c" stroke-width="2.2"><path d="M11 24s8-8 8-14a8 8 0 0 0-16 0c0 6 8 14 8 14z"/><circle cx="11" cy="10" r="3"/></svg>
  </div>
  <div class="pill light">Our Services</div>
  <div class="pill gold">Contact Us</div>
</section>
<div class="abs emblem" aria-hidden="true"></div>

<section class="training">
  <h2 class="section-title">Training <span>&amp;</span> Lessons</h2>
  <p class="lead">Lorem ipsum dolor sit amet, consetetur sadipscing elitr, sed<br>diam nonumy eirmod tempor invidunt ut labore et dolore magna</p>
  <div class="offer" style="left:120px">
    <h3>Training</h3>
    <p>Linden Ridge offers both full and half time training options with Hanna Westbrook. There is much flexibility with both rides and/or lessons weekly in the training packages...</p>
    <div class="btn">Know More</div>
  </div>
  <div class="abs divider-v"></div>
  <div class="offer" style="left:675px">
    <h3>Lessons</h3>
    <p>Lessons are available for all ages of riders. Hanna thoroughly enjoys working with accomplished riders looking to succeed in the show ring, as well as riders...</p>
    <div class="btn">Read More</div>
  </div>
</section>

<section class="about">
  <div class="abs photo" role="img" aria-label="Photo of the trainer riding a pinto horse outdoors beside a barn"></div>
  <h2 class="abs">About Us</h2>
  <div class="abs rule"></div>
  <div class="abs social" aria-label="Social links"><i></i><i></i><i></i></div>
  <div class="abs copy">
    <p>International rider and trainer, Hanna Westbrook began her riding career at a young age. She went up through the ranks of Junior Riders Club and with an emphasis and focus in eventing. During college, Hanna worked for a small breeder starting young horses. Hanna loves starting young horses including starting and guiding them in a correct and quiet way to help them flourish. Her training focuses on gymnastic training incorporating ground work/lunging/long lining, jumping, cavelletti and regular hacking and trail riding.</p>
    <p>Hanna is a NDF Silver Medalist having competed through the international levels of I1. A learner at heart, Hanna regularly clinics and rides with other trainers and accomplished dressage riders from across the nation to continue to pursue her goal of competing at the Grand Prix.</p>
    <p>Hanna has attended the NDF L Program as well as the Instructor/Trainer program to continue her growth as a trainer and rider. Hanna trains and competes yearly in the winter season in Palm Harbor Ridge to further her knowledge and development to share with her students!</p>
  </div>
</section>

<section class="partners">
  <h2 class="section-title">Partnerships</h2>
  <div class="partner" style="left:120px">
    <h3>Fairmont Saddlery</h3>
    <p>Fairmont Saddlery is constantly designing and researching saddles and riders to find the right blend of design and craftsmanship to fit today's demands. Every saddle's detail is carefully checked to be sure the workmanship and quality is there. All saddles are anatomically designed for horse and rider, hand-crafted from the finest leathers, and manufactured using the most technically advanced methods and features available.</p>
  </div>
  <span class="readmore" style="left:120px">Read More</span>
  <div class="abs partner-badge" style="left:378px;top:406px" role="img" aria-label="Partner badge"></div>
  <div class="partner" style="left:685px">
    <h3>Ashford's Saddlery</h3>
    <p>My goal is to provide the best possible fit for both horse and rider whether it is a saddle you already own, one you have on trial, or one that I carry. Being a Qualified Saddle Fitter by the Guild of Saddle Makers allows me to work with all saddle types and brands. In addition, I carry a broad range of saddles to fit your needs, both new and used. Having a multitude of saddles in my stock makes saddle shopping much easier for you.</p>
  </div>
  <span class="readmore" style="left:686px">Read More</span>
  <div class="abs partner-badge" style="left:968px;top:406px" role="img" aria-label="Partner badge"></div>
</section>

<section class="sale">
  <h2 class="section-title">For Sale</h2>
  <div class="sub">Northern Cadence</div>
  <div class="abs copy">
    <p>Northern Cadence, “Cade,” (Corsair x Silver Pilot) is a 2012, 16hh imported Hanoverian. Cade is an incredibly quiet and kind horse. He is ridden by both an amatuer and child rider. He loves to hack and is very quiet alone and with a group of horses. He has shown through first level with scores into the 70's at both training and first level.</p>
    <p>Cade is currently solidly schooling all of second level, as well as half passes and flying changes from third level. Cade has 3 very easy to ride gaits and it is easy for riders to sit his trot. Very quiet and well mannered on the ground with vet, farrier and clipping. He has lovely confirmation with a striking head. He is regularly admired at shows! Cade is very versatile and game and also loves to jump!</p>
  </div>
  <div class="abs photo" role="img" aria-label="Photo of a dark bay gelding standing in front of flowering shrubs"></div>
</section>

<section class="faq">
  <h2 class="section-title">FAQs</h2>
  <div class="abs bracket"></div>
  <div class="q" style="top:155px">How long is the training course ?</div>
  <div class="q" style="top:223px">How much is the training fee ?</div>
  <div class="q" style="top:291px">How many trainees are there ?</div>
  <div class="abs arrow-dot"><svg width="28" height="28" viewBox="0 0 28 28"><path d="M12 9l5 5-5 5" fill="none" stroke="#fff" stroke-width="2"/></svg></div>
  <div class="abs answer">Lorem ipsum dolor sit amet, consetetur sadipscing elitr, sed diam nonumy eirmod tempor invidunt ut labore et dolore magna aliquyam erat, sed diam voluptua. At vero eos et accusam et justo duo dolores et ea rebum. Stet clita kasd gubergren, no sea takimata sanctus est Lorem ipsum dolor sit amet. Lorem ipsum dolor sit amet, consetetur sadipscing elitr, sed diam nonumy eirmod tempor invidunt ut</div>
</section>

<section class="news">
  <h2 class="section-title">Latest News</h2>
  <p class="lead">Lorem ipsum dolor sit amet, consetetur sadipscing elitr, sed<br>diam nonumy eirmod tempor invidunt ut labore et dolore magna</p>
  <div class="card" style="left:120px">
    <p>Lorem ipsum dolor sit amet, consetetur sadipscing elitr, sed diam nonumy eirmod tempor invidunt ut labore et dolore magna aliquyam erat, sed diam voluptua. At vero</p>
    <hr><span class="day">SAT</span><span class="date">February 10</span>
  </div>
  <div class="card" style="left:458px">
    <p>Lorem ipsum dolor sit amet, consetetur sadipscing elitr, sed diam nonumy eirmod tempor invidunt ut labore et dolore magna aliquyam erat, sed diam voluptua. At vero</p>
    <hr><span class="day">SUN</span><span class="date">February 11</span>
  </div>
  <div class="card" style="left:795px">
    <p>Lorem ipsum dolor sit amet, consetetur sadipscing elitr, sed diam nonumy eirmod tempor invidunt ut labore et dolore magna aliquyam erat, sed diam voluptua. At vero</p>
    <hr><span class="day">FRI</span><span class="date">February 23</span>
  </div>
  <div class="abs see-more">See more</div>
</section>

<footer class="footer">
  <h2 class="abs">Contact Me</h2>
  <div class="abs rule"></div>
  <p class="abs note">If you are interested in learning more about Linden Ridge's services or availability for training or lessons, please contact us below!</p>
  <div class="abs social" aria-label="Social links"><i></i><i></i><i></i></div>
  <div class="abs phone">+ 555-014-0434</div>
  <nav class="abs footer-links">Home<br>Services<br>About Us<br>News Room<br>Blog<br>Contact Us</nav>
  <div class="abs map" role="img" aria-label="Map of the area around the farm"></div>
  <div class="abs zoom"><span>+</span><span>−</span></div>
  <div class="abs legal">© 2020 Linden Ridge Stables All Rights Reserved.</div>
</footer>

</body>
</html>
```